Signage for a store*

logo on the two sides of the sign
in the middle is the name of the store witch is VORELT
at the bottom of the two logos, one side for location/address and the other side is contact details phone number is 718-392-6107 address is 2974 THE SIGN WILL BEE 15 FEET BY 4 FEET I WOULD LIKE THAT THE
BACKGROUND OF THE SIGN SHOULD HAVE A NICE COLOR BASE
THAT GOES FOR A WINE STORE

```html
<!DOCTYPE html>
<html lang="en">
<head>
<meta charset="utf-8">
<title>VORELT — Store Sign</title>
<link rel="stylesheet" href="https://fonts.googleapis.com/css2?family=Playfair+Display:wght@400;700&display=swap">
<style>
  :root {
    --stage: #5a5a5a;
    --wine: #a2264a;
    --wine-deep: #8a2542;
    --ink: #ffffff;
  }
  * { margin: 0; padding: 0; box-sizing: border-box; }
  html, body {
    width: 1200px;
    height: 446px;
    overflow: hidden;
    background: var(--stage);
  }
  .sign {
    position: absolute;
    left: 0;
    top: 63px;
    width: 1200px;
    height: 320px;
    background:
      radial-gradient(ellipse 220px 90px at 330px 155px, var(--wine-deep), transparent),
      radial-gradient(ellipse 260px 80px at 640px 120px, var(--wine-deep), transparent),
      radial-gradient(ellipse 200px 90px at 1000px 250px, var(--wine-deep), transparent),
      radial-gradient(ellipse 180px 60px at 160px 20px, var(--wine-deep), transparent),
      var(--wine);
    color: var(--ink);
    font-family: "Playfair Display", serif;
  }
  .sign__name {
    position: absolute;
    left: 0;
    right: 0;
    top: 82px;
    text-align: center;
    font-size: 146px;
    font-weight: 400;
    line-height: 1;
    letter-spacing: 2px;
  }
  .brand-mark {
    position: absolute;
    top: 30px;
    width: 170px;
    height: 220px;
    display: flex;
    flex-direction: column;
    align-items: center;
    justify-content: center;
    gap: 14px;
  }
  .brand-mark--left { left: 68px; }
  .brand-mark--right { left: 962px; }
  .brand-mark__dot {
    width: 54px;
    height: 54px;
    border: 2px solid var(--ink);
    border-radius: 50%;
  }
  .brand-mark__name {
    font-size: 34px;
    font-weight: 400;
    line-height: 1;
    letter-spacing: 1px;
  }
  .sign__detail {
    position: absolute;
    top: 262px;
    width: 240px;
    text-align: center;
    font-size: 31px;
    font-weight: 700;
    line-height: 1;
  }
  .sign__detail--phone { left: 33px; }
  .sign__detail--address { left: 927px; }
</style>
</head>
<body>
  <main class="sign">
    <div class="brand-mark brand-mark--left">
      <span class="brand-mark__dot"></span>
      <span class="brand-mark__name">VORELT</span>
    </div>

    <h1 class="sign__name">VORELT</h1>

    <div class="brand-mark brand-mark--right">
      <span class="brand-mark__dot"></span>
      <span class="brand-mark__name">VORELT</span>
    </div>

    <p class="sign__detail sign__detail--phone">718-392-6107</p>
    <p class="sign__detail sign__detail--address">2974</p>
  </main>
</body>
</html>
```